SPARK - and the compass of quiet days

I´m writing a book about CHANGE and the skills leaders needs to embody the transformation from being amanager to become leaders.
The title of the book in Icelandic is the same as the name of the project (which I want to be used on the designes is:) HAFALDAN
(with the subtitle:) og listin að hlusta

Change is not controlled or managed – Leading effective change is an art form which is one of the big reasons for why 70% of changes within companies fail. The main reason however, is that managers are tasked with managing and directing them. The art form of change is to put it in the hands of leaders who possess the emotional intelligence that is needed – all their other advantages intact – to lead change all the way.

The big problem when it comes to change is that there are too many managers and too few leaders within companies – leaders who possess emotional intelligence which is the most important skill a leader embodies to empower change. A leader has what it takes to empower followership.

A manager tends to push and control, make decisions that he presupposes others to implement the way he expects. An emotionally competent leader leads by example and enhances followership on that journey because of the trust and respect he has earned.

In few words: SOFT SKILLS ARE THE NEW HARD SKILLS!

```html
<!DOCTYPE html>
<html lang="is">
<head>
<meta charset="UTF-8">
<title>HAFALDAN – og listin að hlusta</title>
<link rel="stylesheet" href="https://fonts.googleapis.com/css2?family=Montserrat:wght@400;500;700&display=swap">
<style>
  :root {
    --paper: #ffffff;
    --spine-orange: #f7962f;
    --title-red: #ee4e2e;
    --ink-maroon: #6e1414;
    --wave-teal: #74afa9;
    --wave-coral: #ee5030;
  }
  html, body {
    margin: 0;
    padding: 0;
    overflow: hidden;
    background: var(--paper);
  }
  .cover {
    position: relative;
    width: 800px;
    height: 1200px;
    background: var(--paper);
    overflow: hidden;
    font-family: "Montserrat", sans-serif;
  }
  .spine-band {
    position: absolute;
    top: 0;
    left: 0;
    width: 55px;
    height: 100%;
    background: var(--spine-orange);
  }
  .spine-stripe {
    position: absolute;
    top: 0;
    height: 100%;
    background: var(--spine-orange);
  }
  .spine-stripe--first { left: 63px; width: 13px; }
  .spine-stripe--second { left: 81px; width: 12px; }
  .title-line {
    position: absolute;
    left: 136px;
    margin: 0;
    font-weight: 700;
    font-size: 150px;
    line-height: 1;
    color: var(--title-red);
    letter-spacing: -0.01em;
    white-space: nowrap;
  }
  .title-line--top { top: 112px; }
  .title-line--bottom { top: 237px; }
  .subtitle {
    position: absolute;
    left: 139px;
    top: 429px;
    margin: 0;
    font-weight: 400;
    font-size: 44px;
    line-height: 1;
    color: var(--ink-maroon);
    white-space: nowrap;
  }
  .illustration {
    position: absolute;
    left: 139px;
    top: 597px;
    width: 611px;
    height: 410px;
  }
  .author-name {
    position: absolute;
    right: 52px;
    top: 1104px;
    margin: 0;
    font-weight: 500;
    font-size: 42px;
    line-height: 1;
    letter-spacing: 0.19em;
    color: var(--ink-maroon);
    white-space: nowrap;
  }
</style>
</head>
<body>
  <main class="cover">
    <div class="spine-band"></div>
    <div class="spine-stripe spine-stripe--first"></div>
    <div class="spine-stripe spine-stripe--second"></div>

    <h1 class="book-title">
      <span class="title-line title-line--top">HAF</span>
      <span class="title-line title-line--bottom">ALDAN</span>
    </h1>
    <p class="subtitle">og listin að hlusta</p>

    <svg class="illustration" viewBox="0 0 611 410" role="img"
         aria-label="Illustration: a small figure climbing a rising path of stepping stones, from a red square through teal rounded shapes toward a large coral circle">
      <defs>
        <linearGradient id="stepping-stones-tone" x1="0" y1="1" x2="1" y2="0">
          <stop offset="0" stop-color="#ffffff"/>
          <stop offset="0.35" stop-color="#e4f0ee"/>
          <stop offset="0.7" stop-color="#cfe5e2"/>
          <stop offset="1" stop-color="#fbd9cf"/>
        </linearGradient>
      </defs>
      <rect width="611" height="410" fill="url(#stepping-stones-tone)"/>
    </svg>

    <p class="author-name">AUTHOR NAME</p>
  </main>
</body>
</html>
```